Motor Mate 4x6 Flyer

Need 4 x 6 Flyer with following language:

Willow Crest Motor Mate
Our Motor Mate Will Come to Your Home
Our Motor Mate will Drive Your Car to Nearest Gas Station
Our Motor Mate will Fill-up Your Car with Gas
Our Motor Mate will Immediately Return Your Car
Your Car Covered with $100k of Commercial Insurance
Member Dunmore Chamber of Commerce / Honest Merchant League
www.willowcrestmotormate.example

Place logos of Vortan, Brenn & Dorvane on Left Side of Flyer starting at top left corner, mid left side, left bottom corner.
Place logos of BoltNest, 12-Forty, Tesmira on opposite side right.....
Place Willow Crest Motor Mate Logo on both sides of very top that says Willow Crest Motor Mate

Target Market(s)

Upscale Home Owners

Font styles to use
Sans Serif

Colors
F0912C
F2A743
F7CA91
FBE8D2
FDF5EE

Requirements
Must have
• Flyer Must be Bright Orange

```html
<!DOCTYPE html>
<html lang="en">
<head>
<meta charset="utf-8">
<title>Motor Mate Flyer</title>
<link rel="stylesheet" href="https://fonts.googleapis.com/css2?family=Oswald:wght@300;400;500;600;700&display=swap">
<style>
  :root {
    --backdrop: #bfc0c2;
    --brand-orange: #f0912c;
    --brand-orange-deep: #e07a12;
    --orange-soft: #f2a743;
    --panel-dark: #333233;
    --panel-light: #fdf5ee;
    --ink: #2e2e30;
    --white: #ffffff;
  }
  * { margin: 0; padding: 0; box-sizing: border-box; }
  html, body { width: 1059px; height: 1200px; overflow: hidden; }
  body {
    background: var(--backdrop);
    font-family: "Oswald", "Arial Narrow", sans-serif;
    position: relative;
  }
  .flyer {
    position: absolute;
    left: 247px; top: 176px;
    width: 565px; height: 847px;
    background: var(--panel-light);
    overflow: hidden;
  }
  .hero {
    position: absolute; left: 0; top: 0;
    width: 565px; height: 429px;
    background: var(--panel-dark);
  }
  .hero-photo {
    position: absolute; left: 180px; top: 0;
    width: 385px; height: 420px;
    background:
      radial-gradient(ellipse 90px 120px at 310px 150px, #dcdad8 0%, #c9c6c3 60%, rgba(0,0,0,0) 100%),
      linear-gradient(90deg, #333233 0%, #4a4747 18%, #2a2829 45%, #1f1e1f 70%, #3a3839 100%);
  }
  .hero-fade {
    position: absolute; left: 0; top: 420px;
    width: 565px; height: 9px;
    background: linear-gradient(90deg, var(--panel-dark) 15%, #9a9a9a 60%, var(--white) 100%);
  }
  .brand-box {
    position: absolute; left: 28px; top: 0;
    width: 246px; height: 181px;
    background: var(--brand-orange);
    border-bottom-left-radius: 36px;
    display: flex; flex-direction: column;
    align-items: center; justify-content: center; gap: 14px;
  }
  .brand-mark {
    width: 44px; height: 44px;
    border: 4px solid var(--white);
    border-radius: 8px;
  }
  .brand-name {
    color: var(--white);
    font-weight: 600;
    font-size: 30px;
    letter-spacing: 1px;
    line-height: 1;
  }
  .headline {
    position: absolute; left: 35px; top: 212px;
    color: var(--white);
    line-height: 1;
  }
  .headline .thin {
    display: block;
    font-weight: 400;
    font-size: 31px;
    letter-spacing: 7.6px;
  }
  .headline .bold {
    display: block;
    font-weight: 700;
    font-size: 49px;
    letter-spacing: -1.5px;
    margin: 4px 0 2px;
  }
  .headline .bold.last { margin-bottom: 0; }
  .services-tab {
    position: absolute; left: 28px; top: 446px;
    height: 43px;
    background: var(--brand-orange);
    clip-path: polygon(0 0, 100% 0, calc(100% - 20px) 100%, 0 100%);
    color: var(--white);
    font-weight: 600;
    font-size: 19px;
    letter-spacing: -0.3px;
    line-height: 43px;
    padding: 0 30px 0 9px;
    white-space: nowrap;
  }
  .service-list {
    position: absolute; left: 37px; top: 498px;
    list-style: none;
    color: var(--ink);
    font-size: 20.5px;
    font-weight: 400;
    letter-spacing: -0.2px;
  }
  .service-list li {
    position: relative;
    padding-left: 14px;
    height: 31px;
    line-height: 31px;
    white-space: nowrap;
  }
  .service-list li.spaced { margin-top: 3px; }
  .service-list li::before {
    content: "";
    position: absolute; left: 0; top: 8px;
    width: 7px; height: 7px;
    border-radius: 50%;
    background: var(--brand-orange);
  }
  .membership {
    position: absolute; left: 50px; top: 658px;
    color: var(--ink);
    font-size: 20.5px;
    letter-spacing: -0.2px;
    white-space: nowrap;
  }
  .website {
    position: absolute; left: 50px; top: 692px;
    color: var(--brand-orange-deep);
    font-weight: 600;
    font-size: 27px;
    letter-spacing: -0.5px;
    white-space: nowrap;
  }
  .partners {
    position: absolute; left: 0; top: 745px;
    width: 565px; height: 102px;
    background: var(--white);
    border-top: 4px solid var(--brand-orange);
    border-bottom: 8px solid var(--brand-orange);
    display: flex; align-items: center; justify-content: space-around;
    padding: 0 14px;
  }
  .partner {
    display: flex; align-items: center; gap: 5px;
    color: var(--ink);
    font-weight: 600;
    font-size: 20px;
    white-space: nowrap;
  }
  .partner-dot {
    width: 10px; height: 10px;
    border-radius: 50%;
    background: var(--brand-orange);
  }
</style>
</head>
<body>
  <main class="flyer">
    <section class="hero">
      <div class="hero-photo" role="img" aria-label="Photo of a valet in a black tuxedo and white gloves holding out a car key"></div>
      <div class="hero-fade"></div>
      <div class="brand-box">
        <div class="brand-mark"></div>
        <div class="brand-name">MOTOR MATE</div>
      </div>
      <h1 class="headline">
        <span class="thin">FUELING YOUR</span>
        <span class="bold">CONVENIENCE</span>
        <span class="thin">WHERE SERVICE</span>
        <span class="bold last">MEETS SPEED!</span>
      </h1>
    </section>

    <h2 class="services-tab">WILLOW CREST MOTOR MATE SERVICES</h2>

    <ul class="service-list">
      <li>Our Motor Mate Will Come to Your Home</li>
      <li>Our Motor Mate will Drive Your Car to Nearest Gas Station</li>
      <li>Our Motor Mate will Fill-up Your Car with Gas</li>
      <li class="spaced">Our Motor Mate will Immediately Return Your Car</li>
      <li class="spaced">Your Car Covered with $100k of Commercial Insurance</li>
    </ul>
    <p class="membership">Member Dunmore Chamber of Commerce / Honest Merchant League</p>
    <p class="website">www.willowcrestmotormate.example</p>

    <footer class="partners">
      <span class="partner">Brenn</span>
      <span class="partner">Dorvane</span>
      <span class="partner">Vortan</span>
      <span class="partner"><span class="partner-dot"></span>BoltNest</span>
      <span class="partner">12-Forty</span>
      <span class="partner">Tesmira</span>
    </footer>
  </main>
</body>
</html>
```